Company letter head

Hello,
We are a global logistics company requiring a letterhead design for all our company documentation.
Company Name: Clearly display the full name of your company at the top of the letterhead.
Logo: Include your company logo for brand recognition.
Contact Information: This includes your company's address, phone number, email address, and website URL.
Target Market(s)
Clients/customers
Industry/Entity Type
Logistics
Font styles to use
Sans Serif
Requirements
Must have
- Company name and logo
Nice to have
- borders, header/footers

```html
<!DOCTYPE html>
<html lang="en">
<head>
<meta charset="utf-8">
<title>Northwind Freight Lines – Letterhead</title>
<link href="https://fonts.googleapis.com/css2?family=Open+Sans:wght@400;700&display=swap" rel="stylesheet">
<style>
  :root {
    --brand-red: #d71f26;
    --brand-charcoal: #3c3c3c;
    --paper: #ffffff;
    --backdrop: #cfcfcf;
    --ink: #1e1e1e;
  }
  * { margin: 0; padding: 0; box-sizing: border-box; }
  html, body {
    width: 1200px;
    height: 686px;
    overflow: hidden;
    background: var(--backdrop);
    font-family: "Open Sans", sans-serif;
  }
  .canvas {
    position: relative;
    width: 1200px;
    height: 686px;
  }
  .letterhead {
    position: absolute;
    left: 370px;
    top: 18px;
    width: 460px;
    height: 650px;
    background: var(--paper);
    overflow: hidden;
    box-shadow: 0 4px 18px rgba(0,0,0,0.18);
  }
  .letterhead__brand {
    position: absolute;
    top: 38px;
    right: 40px;
    display: flex;
    align-items: center;
    gap: 8px;
  }
  .brand-mark {
    width: 12px;
    height: 12px;
    background: var(--brand-red);
  }
  .brand-name {
    font-weight: 700;
    font-size: 15px;
    letter-spacing: 0.06em;
    text-transform: uppercase;
    color: var(--brand-red);
  }
  .letterhead__wave {
    position: absolute;
    left: 0;
    bottom: 0;
    width: 460px;
    height: 230px;
  }
  .letterhead__contact {
    position: absolute;
    right: 40px;
    bottom: 92px;
    list-style: none;
    text-align: right;
    font-size: 10.5px;
    line-height: 1.5;
    color: var(--ink);
  }
  .contact-item {
    display: flex;
    justify-content: flex-end;
    align-items: flex-start;
    gap: 7px;
  }
  .contact-icon {
    width: 11px;
    height: 11px;
    margin-top: 2px;
    flex: none;
    fill: var(--brand-red);
  }
  .contact-spacer { width: 11px; flex: none; }
</style>
</head>
<body>
<main class="canvas">
  <article class="letterhead">
    <header class="letterhead__brand">
      <span class="brand-mark"></span>
      <span class="brand-name">Northwind Freight Lines</span>
    </header>

    <ul class="letterhead__contact">
      <li class="contact-item">
        <span>218 Harbour Lane</span>
        <svg class="contact-icon" viewBox="0 0 12 12" aria-hidden="true"><path d="M6 0.5a4 4 0 0 1 4 4c0 3-4 7-4 7s-4-4-4-7a4 4 0 0 1 4-4zm0 2.3a1.7 1.7 0 1 0 0 3.4a1.7 1.7 0 0 0 0-3.4z"/></svg>
      </li>
      <li class="contact-item">
        <span>Chatham, Kent, ME4 2QT</span>
        <span class="contact-spacer"></span>
      </li>
      <li class="contact-item">
        <span>(555) 014-2290</span>
        <svg class="contact-icon" viewBox="0 0 12 12" aria-hidden="true"><path d="M2.6 0.8l1.8 0.2 0.9 2.6-1.3 1a7 7 0 0 0 3.4 3.4l1-1.3 2.6 0.9 0.2 1.8c-0.2 1-1.2 1.8-2.2 1.6C4.7 10.4 1.6 7.3 1 3.5 0.8 2.4 1.6 1 2.6 0.8z"/></svg>
      </li>
      <li class="contact-item">
        <span>www.northwindfreight.com</span>
        <svg class="contact-icon" viewBox="0 0 12 12" aria-hidden="true"><path d="M6 0.5a5.5 5.5 0 1 0 0 11a5.5 5.5 0 0 0 0-11zm0 1.2c0.7 0.8 1.2 2.2 1.3 3.7H4.7C4.8 3.9 5.3 2.5 6 1.7zM4.7 6.6h2.6C7.2 8.1 6.7 9.5 6 10.3 5.3 9.5 4.8 8.1 4.7 6.6zM1.8 5.4a4.3 4.3 0 0 1 1.9-3.1c-0.3 0.9-0.5 2-0.6 3.1zm0 1.2h1.3c0.1 1.1 0.3 2.2 0.6 3.1a4.3 4.3 0 0 1-1.9-3.1zm8.4-1.2H8.9c-0.1-1.1-0.3-2.2-0.6-3.1a4.3 4.3 0 0 1 1.9 3.1zm0 1.2a4.3 4.3 0 0 1-1.9 3.1c0.3-0.9 0.5-2 0.6-3.1z"/></svg>
      </li>
      <li class="contact-item">
        <span>info@northwindfreight.com</span>
        <svg class="contact-icon" viewBox="0 0 12 12" aria-hidden="true"><path d="M0.8 2.5h10.4v7H0.8zm0.9 0.9v0.3L6 6.8l4.3-3.1v-0.3zm0 1.4v3.8h8.6V4.8L6 7.9z"/></svg>
      </li>
    </ul>

    <svg class="letterhead__wave" viewBox="0 0 460 230" preserveAspectRatio="none" aria-hidden="true">
      <path d="M0 38 C 18 120, 90 165, 230 196 C 330 216, 395 222, 435 230"
            fill="none" stroke="var(--brand-charcoal)" stroke-width="9"/>
      <path d="M0 160 C 40 195, 110 200, 200 188 C 300 176, 370 205, 408 230 L 0 230 Z"
            fill="var(--brand-red)"/>
    </svg>
  </article>
</main>
</body>
</html>
```